Business Card design for amazing new Dental Office

Please read this brief closely!

Our client is a modern new dental office/
They love their new logo.
Now it's time to create a business card for them.

It should be a two sided card:
Side one should have the logo and name and maybe a color background or design.
Side two should have all the contact information which is here:

Marcus Pellow, D.D.S
General and Cosmetic Dentistry
4178 W. Orchard Lane
Seabrook, CA 95021
(707) 219-4862
drmarc@bluefernsmiles.example
www.bluefernsmiles.example

Feel free to arrange that info as you like and to style both sides of the card according to your creativity. This is a chance for you to show your design skills!

Client is open to font choices and is looking for a style that is amazing and premium. Colors can be selected from the logo, or any variation of those.

You will not win this contest with a less than beautiful card design so please feel free to make multiple submissions.

Logo files attached and please message me with any questions.
Thanks!

Target Market(s)

Families and Professionals seeking dental services

Industry/Entity Type

Dental

Contact Information for Business Card

Logo, style, contact info as per the brief

Font styles to use
Sans Serif

Requirements
Must have
• Client's logo and contact details as per brief
Nice to have
• Unique style reflecting high end dental clinic near the beach
Should not have
• Must not look like a template

```html
<!DOCTYPE html>
<html lang="en">
<head>
<meta charset="utf-8">
<title>Blue Fern Smiles – Business Card</title>
<link rel="stylesheet" href="https://fonts.googleapis.com/css2?family=Source+Sans+3:wght@400;700&display=swap">
<style>
  :root {
    --backdrop: #3e7684;
    --paper: #f1f1f1;
    --brand-grey: #9a9a9a;
    --accent-blue: #3f9fc4;
    --link-blue: #3a9fd8;
    --wash-blue: #c3dbe6;
    --ink: #3c3c3c;
  }
  * { margin: 0; padding: 0; box-sizing: border-box; }
  html, body { width: 1200px; height: 1200px; overflow: hidden; }
  body {
    background: var(--backdrop);
    font-family: "Source Sans 3", "Source Sans Pro", Arial, sans-serif;
    display: flex;
    flex-direction: column;
    align-items: center;
    justify-content: center;
    gap: 72px;
  }
  .card {
    position: relative;
    width: 860px;
    height: 491px;
    background: var(--paper);
    overflow: hidden;
  }

  /* Front side */
  .card-front { display: flex; flex-direction: column; align-items: center; }
  .front-brand {
    margin-top: 190px;
    display: flex;
    align-items: center;
    gap: 18px;
    color: var(--brand-grey);
    font-weight: 400;
    font-size: 58px;
    letter-spacing: 4px;
    text-transform: uppercase;
  }
  .brand-dot {
    width: 22px; height: 22px; border-radius: 50%;
    background: var(--accent-blue);
  }
  .front-url {
    margin-top: 96px;
    color: var(--link-blue);
    font-size: 26px;
    letter-spacing: 6px;
  }

  /* Back side */
  .back-wash {
    position: absolute;
    left: 0;
    top: 0;
    width: 440px;
    height: 290px;
    background: linear-gradient(160deg, var(--wash-blue) 0%, rgba(195, 219, 230, 0.35) 60%, rgba(241, 241, 241, 0) 100%);
  }
  .back-brand {
    position: absolute;
    left: 60px;
    top: 340px;
    display: flex;
    align-items: center;
    gap: 12px;
    color: var(--brand-grey);
    font-size: 32px;
    letter-spacing: 2px;
    text-transform: uppercase;
  }
  .back-brand .brand-dot { width: 13px; height: 13px; }
  .contact {
    position: absolute;
    left: 480px;
    top: 78px;
    color: var(--ink);
    font-size: 19px;
    line-height: 1.3;
  }
  .contact-name {
    color: var(--accent-blue);
    font-weight: 700;
    font-size: 34px;
    line-height: 1.1;
  }
  .contact-role { font-size: 19px; margin-bottom: 26px; margin-left: 8px; }
  .contact-block { margin-left: 20px; margin-bottom: 26px; }
</style>
</head>
<body>

  <section class="card card-front">
    <div class="front-brand"><span class="brand-dot"></span>Blue Fern Smiles</div>
    <div class="front-url">www.bluefernsmiles.example</div>
  </section>

  <section class="card card-back">
    <div class="back-wash" role="img" aria-label="Soft pale blue decorative wave area"></div>

    <div class="back-brand"><span class="brand-dot"></span>Blue Fern Smiles</div>

    <div class="contact">
      <div class="contact-name">Marcus Pellow, D.D.S</div>
      <div class="contact-role">General and Cosmetic Dentistry</div>
      <div class="contact-block">
        4178 W. Orchard Lane<br>
        Seabrook, CA 95021<br>
        (707) 219-4862
      </div>
      <div class="contact-block">
        drmarc@bluefernsmiles.example<br>
        www.bluefernsmiles.example
      </div>
    </div>
  </section>

</body>
</html>
```